Vesk Architecture

We are a architectural design and build company working between scales 1/1000 to 1/1 we want people to understand our difference from our design experience and quality.we build hotels restourants and office spaces.Our company name is Vesk architecture to mind sustainability.

We want to write our adress phone and work spesifications on the card and we want our logo as backround.

Ps:you could find the logo adress and phone box numbers from the web:www.veskmimarlik-ornek.com

Target Market(s)

Who looks for experts.

Industry/Entity Type

Architecture

Requirements
Must have
• Design is over everything.
Should not have
• we don want it to be colorfull

```html
<!DOCTYPE html>
<html lang="tr">
<head>
<meta charset="utf-8">
<title>Vesk Architecture – Business Card</title>
<link rel="stylesheet" href="https://fonts.googleapis.com/css2?family=Barlow:wght@400;600&display=swap">
<style>
  :root {
    --backdrop: #ececec;
    --ink: #111111;
    --paper: #ffffff;
    --mark-grey: #d9d9d9;
    --text-grey: #222222;
  }
  * { margin: 0; padding: 0; box-sizing: border-box; }
  html, body {
    width: 1200px;
    height: 920px;
    overflow: hidden;
    background: var(--backdrop);
    font-family: "Barlow", "Helvetica Neue", Arial, sans-serif;
  }
  .canvas {
    position: relative;
    width: 1200px;
    height: 920px;
  }
  .card {
    position: absolute;
    width: 500px;
    height: 345px;
  }
  .card--front {
    left: 80px;
    top: 250px;
    background: var(--ink);
    color: var(--paper);
  }
  .card--back {
    left: 620px;
    top: 330px;
    background: var(--paper);
    color: var(--text-grey);
    box-shadow: 0 0 0 1px #dedede;
  }
  .wordmark {
    position: absolute;
    left: 38px;
    top: 92px;
    font-weight: 400;
  }
  .wordmark__name {
    display: block;
    font-size: 118px;
    line-height: 1;
    letter-spacing: -2px;
  }
  .wordmark__sub {
    display: block;
    margin-top: 8px;
    margin-left: 6px;
    font-size: 28px;
    letter-spacing: 4px;
  }
  .contact {
    position: absolute;
    left: 52px;
    top: 100px;
  }
  .contact__name {
    font-size: 16px;
    font-weight: 600;
    color: var(--ink);
    line-height: 1.2;
  }
  .contact__role {
    font-size: 15px;
    font-weight: 400;
    line-height: 1.2;
  }
  .contact__mark {
    display: block;
    width: 58px;
    height: 58px;
    margin: 12px 0 10px 6px;
  }
  .contact__lines {
    list-style: none;
    font-size: 15px;
    line-height: 19px;
  }
  .contact__label {
    font-weight: 600;
    color: var(--ink);
  }
</style>
</head>
<body>
<main class="canvas">
  <section class="card card--front" aria-label="Card front">
    <div class="wordmark">
      <span class="wordmark__name">vesk</span>
      <span class="wordmark__sub">MİMARLIK</span>
    </div>
  </section>

  <section class="card card--back" aria-label="Card back">
    <div class="contact">
      <p class="contact__name">Deniz Arman YALCIN</p>
      <p class="contact__role">Mimar</p>
      <svg class="contact__mark" viewBox="0 0 58 58" aria-hidden="true">
        <circle cx="29" cy="29" r="27" fill="var(--mark-grey)"/>
      </svg>
      <ul class="contact__lines">
        <li>Rasimpasa Mah. Yeldegirmeni Cad. Lale Sok.</li>
        <li>No: 7 Kadıköy / ISTANBUL</li>
        <li><span class="contact__label">t.</span> 0216 000 41 52</li>
        <li><span class="contact__label">f.</span> 0216 000 41 53</li>
        <li><span class="contact__label">e.</span>veskmimarlik@ornek-mail.com</li>
      </ul>
    </div>
  </section>
</main>
</body>
</html>
```